Mobile Repair Service on location needs a Web Design

We are starting a new mobile device repair service called Gadget Haven and our website needs a design!

Hello Designers!
First, we'd like to make clear this is more than a simple web design contest, we want the designers to create an idea. We want someone who can create the whole theme of the service's we provide. We want someone that can help design our visual branding, help us communicate a sentiment. And we are willing to pay for that.

Who are we?
Our company is based in Rotterdam, the Netherlands. We provide different services for all kinds of electronic devices. The kind of services we provide are, among other things, installations of hardware and software and the repair of broken or malfunctioning devices.
We are starting a new service that offers mobile device repairs on location, be it at the home of our customers, their office, or any other place. Just give us the address and we will come to you for the repair job. This is also our main USP. We have multiple skilled engineers who drive trough the country on a daily basis and can be on location within a working day. Repair is done immediately onsite while the customer waits. At this stage we will start with the smartphone product-group within the mobile devices. In a second phase we might also add tablets.
People don't want to be without their phone for weeks because of some parts that needed to be ordered by a repair center they had to sent their phone to. We offer a fully functional mobile repair center in the form of specially customized vans. These vans have all the tools and utilities needed by our engineers to safely repair your mobile device. Your phone is being repaired directly in front of you, the next business-day, on a location you desire.

For this new service we are creating a website called Gadget Haven. The website needs a story and matching design and this is where you come in. We are not looking for a simple template design we can get from any place. We need a story. We want you to create an idea, build a unique theme or vision that helps sell the product/service. This goes beyond the design of the website. We need the whole package, the design you are creating needs to have returning elements like icons, color use, images, maybe even characters etc. You name it! There needs to be a common thread in the design so we can reuse elements in, for example, the email templates, the work order or receipt we give to our customers (we may contact the winner of the contest to design these for us as well!).

The name 'Gadget Haven' is chosen. Haven (short for rehabilitate) has a bold and playful tone to it and the design needs to reflect the name. So we're looking for a somewhat playful and cheeky design. Definitely not too serious and definitely modern. We already got a logo that we love and that fit's this description (see attached design documents for the logo). It's bold, powerful and fun. Our web design needs to reflect this as well and has to fit in with our logo.
We would really like it if the design somehow incorporates elements that highlight our unique selling points (repairs on location, we come to you etc.). We would really like some form of story telling in the design. Think clumsy people breaking their phones. Teenagers in tears because they have no access to their friends. People nowadays have the need to always be 'connected'. What happens when your phone is broken or malfunctioning? We're handling tech, we are nerds and a little bit weird, but we're professionals and here to help you with your problem. The sentiment Wire Troop tries to communicate is something we really like. We're looking for fresh idea's, anything goes!

In an overview all Unique Selling Points of the Gadget haven service:
- Professional service on location. Don’t ship to us we will come to you!
- Clear pricing upfront. No hidden cost.
- Next business-day repair.
- Backed by a professional call center open 12 hours a day and open on a Saturday as well
- Backed by a professional repair center with more then 12 years of experience
- Repair is done by certified engineers
- 1 year warranty on the repair

The process:
The main function of our website will be for customers to make a repair request. A customer will visit our website and can make a repair request immediately by going through a 'request-order-flow'. In this flow he or she will need to fill in some forms and can select wich type/model/brand of mobile device he or she has and what parts need to be repaired. After a request is placed we will call the customer back (within an hour) for a short intake and to set a date/time and location. Our engineer will meet the customer at the specified location and will repair the device onsite in one of our mobile repair centers, which is a specialized van equipped with all the tools needed for device restorations.
So in short the steps are:
- Choose your device and repair job
- Place the order
- Get a callback within the hour
- Set date and location
- We will come to you.

Website functionality:
Our website is our main form of communication. So the sentiment we want to communicate needs be reflected in the design. We need a main/front page designed (preferably a long scrolling page design) containing:
1. Customers will be able to request a repair job directly on our website. So there will need to be a prominent button/link at the top of our main page that will bring the customer to this 'request-order-flow'. This is the main flow which needs to be full focus on the front page. All other items are secondary.
2. The general information of who we are and what we do, and why the customer should choose us. Preferably in short bullet-point type keywords/sentences with icons or other visual cues. See our unique selling points to get an idea of the information that will be displayed here.
3. There needs to be a section that will explain the process (see above) of a repair request step-by- step, again in brief short key sentences and with (custom) icons.
4. There needs to be a section that explains to the customer he/she can always contact us if they are not sure what the problem is with their device, and for this reason are not sure what repair request they should order.
5. We want to implement some functionality that display customer ratings or customer reviews. So there needs to be room for some kind of widget of plugin we're going to implement which shows these reviews.
6. A 'For business section' where we will explain all the options we provide for corporate clients.
7. Social media links.
8. There needs to be a menu with buttons that leads to the all sections described in the previous points.

For now, we need a design for our front page. In the second phase, when we have picked our winner, we may ask the winner to design the page(s) for our request workflow as well.

EDIT:
Finally, we have a very specific order in mind for the different segments of our website. We would like you to add some more segments that were not in our original brief as well:

1. Top header with order/request button. (should instantly make clear our main USP, we do repairs on location)
2. Our process
3. Our unique selling points / why choose us
4. The kind of repairs we do (broken screens, broken batteries, water damage, broken camera's, no sound etc.)
5. A 'meet our team' section, where we introduce some of our engineers
6. A 'contact us for any questions' section/
7. Testimonials/user reviews
8. A section where we show key performance indicators
9. 'For businesses' sections
10.'Subscribe for newsletter' field
11. Social media buttons

Industry/Entity Type

It Service

Number of Pages Required

1 page

Font styles to use
Sans Serif

Requirements
Must have
• a main/front page, design only
• custom icons/images for banners, adverts online and in print (high res)
Nice to have
• Storytelling in our design.
• Design that fits with our brand new logo.
• Elements like icons to have a flat design.
• Keep in mind that the website will need to be responsive when designing! (Ideally provide an example of the mobile design as well)
• Create a fun and trustworthy feeling.

```html
<!DOCTYPE html>
<html lang="en">
<head>
<meta charset="utf-8">
<title>Gadget Haven – Mobile Repair On Location</title>
<link rel="stylesheet" href="https://fonts.googleapis.com/css2?family=Lato:wght@400;700;900&display=swap">
<style>
:root{
  --orange:#f26522;
  --blue:#3d5485;
  --blue-dark:#33466f;
  --navy:#17233f;
  --navy-deep:#0f1a31;
  --ink:#222;
  --grey-text:#a3a3a3;
  --grey-box:#e8e8e8;
  --grey-icon:#6b6b6b;
  --topbar:#3a3a3a;
  --strip:#f0f0f0;
}
*{box-sizing:border-box;margin:0;padding:0}
html,body{width:1200px;height:2564px;overflow:hidden}
body{font-family:'Lato',Arial,sans-serif;color:var(--ink);background:#fff;position:relative}
.abs{position:absolute}
.wrap{position:absolute;left:90px;width:1015px}

/* top bar */
.topbar{top:0;left:0;width:1200px;height:30px;background:var(--topbar);color:#ccc;font-size:11px}
.topbar .welcome{position:absolute;left:90px;top:9px}
.topbar .social{position:absolute;right:95px;top:8px;display:flex;gap:10px;font-size:10px;color:#eee}

/* header */
.header{top:30px;left:0;width:1200px;height:90px;background:#fff}
.brand{position:absolute;left:90px;top:22px;display:flex;align-items:center;gap:10px}
.brand-mark{width:46px;height:46px;border-radius:50%;background:var(--orange)}
.brand-name{font-size:22px;font-weight:900;color:var(--blue);line-height:22px;width:90px}
.contact-item{position:absolute;top:18px;font-size:13px;font-weight:700;color:#333}
.contact-item small{display:block;font-size:11px;font-weight:400;color:#888;margin-top:8px}
.contact-item svg{vertical-align:-2px;margin-right:4px}

/* nav */
.nav{top:120px;left:0;width:1200px;height:47px;background:var(--blue)}
.nav ul{list-style:none;position:absolute;left:90px;top:15px;display:flex;gap:0}
.nav li{color:#fff;font-size:13px;font-weight:700;margin-right:52px}
.nav .request{position:absolute;left:981px;top:0;width:125px;height:47px;background:var(--orange);color:#fff;font-size:13px;font-weight:700;text-align:center;line-height:47px}

/* hero */
.hero{top:167px;left:0;width:1200px;height:348px;background:linear-gradient(90deg,#f1f1f1 0%,#ececec 50%,#e4e4e4 100%)}
.hero-photo{position:absolute;right:0;top:0;width:520px;height:348px;background:linear-gradient(135deg,#dcdcdc,#9a9a9a 55%,#3a3f3a)}
.hero h1{position:absolute;left:90px;top:83px;font-size:35px;font-weight:900;line-height:55px;color:#111}
.btn{display:inline-block;color:#fff;font-size:16px;text-align:center;border-radius:3px}
.hero .btn{position:absolute;left:90px;top:222px;width:154px;height:46px;line-height:46px;background:var(--blue)}
.arrow{position:absolute;top:160px}

/* about */
.section-title{font-size:30px;font-weight:900;color:#333}
.rule{width:68px;height:1px;background:#bbb;margin-top:18px}
.about{top:535px;left:90px;width:500px}
.about-photos{display:flex;gap:6px;margin-top:25px}
.about-photos div{width:160px;height:130px}
.about p{font-size:13.5px;color:var(--grey-text);line-height:22px;margin-top:22px}
.about .tagline{font-size:22px;color:#444;line-height:33px;margin-top:20px}
.about .btn{margin-top:30px;width:178px;height:40px;line-height:40px;background:var(--orange)}

.why{top:535px;left:635px;width:475px}
.why ul{list-style:none;margin-top:22px}
.why li{position:relative;padding-left:38px;margin-bottom:14px}
.why li svg{position:absolute;left:0;top:0}
.why h4{font-size:13px;font-weight:700;line-height:17px;color:#111}
.why p{font-size:12.5px;color:var(--grey-text);line-height:20px;margin-top:4px}
.why .btn{margin-top:8px;width:178px;height:40px;line-height:40px;background:var(--blue)}

/* process */
.process{top:1027px;left:0;width:1200px;height:308px;background:linear-gradient(120deg,#2a3a5e,#1c2a4a 50%,#26375a)}
.process .section-title{color:#fff;text-align:center;position:absolute;top:20px;width:100%}
.process .rule{position:absolute;left:566px;top:66px;background:#7c8bad}
.step{position:absolute;top:98px;width:200px;text-align:center;color:#fff;font-size:15px;font-weight:700}
.step .ring{width:124px;height:124px;border:2px solid #fff;border-radius:50%;margin:0 auto 42px;display:flex;align-items:center;justify-content:center}

/* categories */
.cats-title{top:1355px;left:0;width:1200px;text-align:center}
.cats-title .rule{margin:18px auto 0}
.card{position:absolute;width:322px;height:133px;background:var(--grey-box);display:flex}
.card .icon{width:77px;background:var(--grey-icon);display:flex;align-items:center;justify-content:center}
.card .body{padding:26px 0 0 27px}
.card h5{font-size:14.5px;font-weight:400;color:#333;text-transform:uppercase}
.card p{font-size:11.5px;color:#888;line-height:20px;margin-top:4px}
.card.active{background:var(--blue)}
.card.active .icon{background:var(--orange)}
.card.active h5,.card.active p{color:#fff}

/* testimonials */
.quotes-title{top:1775px;left:0;width:1200px;text-align:center}
.quotes-title .rule{margin:18px auto 0}
.quote{position:absolute;top:1860px;width:329px;height:180px;background:#f3f3f3;padding:12px 28px}
.quote p{font-size:12.5px;font-style:italic;color:#444;line-height:21px}
.avatar{position:absolute;left:24px;top:92px;width:80px;height:80px;border-radius:50%;background:linear-gradient(#c9ccd2,#8a93a3);border:3px solid #fff}
.quote .who{position:absolute;right:22px;top:124px;text-align:right;font-size:14px;color:var(--blue)}
.quote .who span{display:block;color:var(--orange);font-size:12.5px;margin-top:2px}

/* partners */
.partners{top:2090px;left:0;width:1200px;height:132px;background:var(--strip)}
.partner{position:absolute;top:38px;height:56px;background:#cfcfcf;border-radius:4px}

/* footer */
.footer{top:2222px;left:0;width:1200px;height:290px;background:var(--navy);color:#fff}
.footer h6{position:absolute;top:50px;font-size:14px;font-weight:700;letter-spacing:.3px}
.footer .line{position:absolute;font-size:12.5px;font-weight:700;line-height:19px}
.footer .line svg{position:absolute;left:-27px;top:2px}
.links{position:absolute;left:393px;top:92px;list-style:none;font-size:13px;line-height:26.5px;color:#ccd}
.links li:first-child{color:var(--orange)}
.news p{position:absolute;left:614px;top:94px;width:240px;font-size:12.5px;line-height:22px}
.email{position:absolute;left:614px;top:149px;width:226px;height:35px;background:#fff;color:#333;font-size:12.5px;padding:10px 8px}
.subscribe{position:absolute;left:614px;top:206px;width:226px;height:36px;background:var(--orange);font-size:13px;text-align:center;line-height:36px;border-radius:2px}
.follow{position:absolute;left:926px;top:105px;display:flex;gap:12px;font-size:11px}
.follow span:first-child{color:var(--orange)}
.bottom{top:2512px;left:0;width:1200px;height:52px;background:var(--navy-deep);color:#bbb;font-size:13px;text-align:center;line-height:52px}
</style>
</head>
<body>

<div class="abs topbar">
  <span class="welcome">Welcome to Gadget Haven</span>
  <div class="social"><span>Linkr</span><span>Chirpa</span><span>Pixo</span><span>Pinlo</span><span>Vidz</span><span>Plusr</span></div>
</div>

<header class="abs header">
  <div class="brand">
    <div class="brand-mark"></div>
    <div class="brand-name">GADGET HAVEN</div>
  </div>
  <div class="contact-item" style="left:650px">
    <svg width="14" height="11" viewBox="0 0 14 11"><rect x="0" y="0" width="14" height="11" fill="#333"/><path d="M0 0l7 6 7-6" stroke="#fff" fill="none"/></svg>Mail Us Today
    <small>hello@gadgethaven.example</small>
  </div>
  <div class="contact-item" style="left:800px">
    <svg width="10" height="14" viewBox="0 0 10 14"><path d="M5 0a5 5 0 0 1 5 5c0 4-5 9-5 9S0 9 0 5a5 5 0 0 1 5-5z" fill="#333"/><circle cx="5" cy="5" r="2" fill="#fff"/></svg>Company Location
    <small>48 Harbour Lane, Maasport</small>
  </div>
  <div class="contact-item" style="left:988px">
    <svg width="12" height="12" viewBox="0 0 12 12"><rect width="12" height="12" rx="2" fill="#333"/><path d="M3 3l2 0 1 2-1 1c.5 1 1 1.5 2 2l1-1 2 1v2C6 10 2 6 3 3z" fill="#fff"/></svg>+(010) 555 0142
    <small>Call us for more details</small>
  </div>
</header>

<nav class="abs nav">
  <ul><li>Home</li><li>About</li><li>Services</li><li>Experts</li><li>Pricing</li><li>Contact us</li></ul>
  <div class="request">Request</div>
</nav>

<section class="abs hero">
  <div class="hero-photo" role="img" aria-label="Photo of a technician's gloved hands repairing an opened smartphone circuit board"></div>
  <h1>Professional service on location.<br>Don’t ship to us we will come to you!</h1>
  <span class="btn">CONTACT US</span>
  <svg class="arrow" style="left:32px" width="16" height="26" viewBox="0 0 16 26"><path d="M13 2L3 13l10 11" stroke="#666" stroke-width="3" fill="none"/></svg>
  <svg class="arrow" style="left:1140px" width="16" height="26" viewBox="0 0 16 26"><path d="M3 2l10 11L3 24" stroke="#fff" stroke-width="3" fill="none"/></svg>
</section>

<section class="abs about">
  <h2 class="section-title">Who We Are</h2>
  <div class="rule"></div>
  <div class="about-photos">
    <div role="img" aria-label="Photo of hands opening a phone's cracked screen" style="background:linear-gradient(135deg,#d8d8d8,#4a4a4a)"></div>
    <div role="img" aria-label="Photo of a technician testing a phone board with a multimeter" style="background:linear-gradient(135deg,#e8e2d8,#8a7a68)"></div>
    <div role="img" aria-label="Photo of a repair engineer working at a bench" style="background:linear-gradient(135deg,#c7ccd4,#6a7486)"></div>
  </div>
  <p>Our company is based in Rotterdam, the Netherlands. We provide different services for all kinds of electronic devices. The kind of services we provide are, among other things, installations of hardware and software and the repair of broken or malfunctioning devices.</p>
  <div class="tagline">Save time, Save money, With Quality Phone<br>Repair Service,</div>
  <span class="btn">READ MORE</span>
</section>

<section class="abs why">
  <h2 class="section-title">Why Choose Us</h2>
  <div class="rule"></div>
  <ul>
    <li><svg width="24" height="20" viewBox="0 0 24 20"><circle cx="12" cy="10" r="8" fill="none" stroke="#f26522" stroke-width="2.5"/><path d="M4 2l16 16" stroke="#f26522" stroke-width="2.5"/></svg>
      <h4>Clear pricing upfront. No hidden cost.</h4>
      <p>Lorem ipsum dolor sit amet, consectetur adipisicing elit. Earum sunt ut dolorem laboriosam culpa excepturi sed distinctio eius! Ut magnam</p></li>
    <li><svg width="24" height="24" viewBox="0 0 24 24"><circle cx="12" cy="12" r="10" fill="none" stroke="#f26522" stroke-width="2.5"/><path d="M8 7h3l1 3-2 1c1 2 2 3 4 4l1-2 3 1v3c-6 0-10-4-10-10z" fill="#f26522"/></svg>
      <h4>Backed by a professional call center open 12 hours<br>a day and open on a Saturday as well</h4>
      <p>Lorem ipsum dolor sit amet, consectetur adipisicing elit. Earum sunt ut dolorem laboriosam culpa excepturi sed distinctio eius! Ut magnam</p></li>
    <li><svg width="24" height="24" viewBox="0 0 24 24"><path d="M8 3h5l2 4 4 1-1 6-3 2v5H8l-2-6-3-2 2-6z" fill="#f26522"/></svg>
      <h4>Backed by a professional repair center with more then<br>12 years of experience</h4>
      <p>Lorem ipsum dolor sit amet, consectetur adipisicing elit. Earum sunt ut dolorem laboriosam culpa excepturi sed distinctio eius! Ut magnam</p></li>
    <li><svg width="24" height="24" viewBox="0 0 24 24"><circle cx="12" cy="9" r="6" fill="#f26522"/><path d="M8 13l-3 9 4-2 2 3 1-9zM16 13l3 9-4-2-2 3-1-9z" fill="#f26522"/></svg>
      <h4>1 year warranty on the repair</h4>
      <p>Lorem ipsum dolor sit amet, consectetur adipisicing elit. Earum sunt ut dolorem laboriosam culpa excepturi sed distinctio eius! Ut magnam</p></li>
  </ul>
  <span class="btn">VIEW MORE</span>
</section>

<section class="abs process" aria-label="Our process">
  <h2 class="section-title">Our Process</h2>
  <div class="rule"></div>
  <div class="step" style="left:112px"><div class="ring">
    <svg width="50" height="50" viewBox="0 0 50 50" fill="none" stroke="#fff" stroke-width="2.5"><rect x="6" y="6" width="26" height="38" rx="3"/><rect x="28" y="18" width="16" height="26" rx="2"/></svg></div>Choose your device and repair job</div>
  <div class="step" style="left:325px"><div class="ring">
    <svg width="40" height="50" viewBox="0 0 40 50"><path d="M20 4a14 14 0 0 1 14 14c0 12-14 28-14 28S6 30 6 18A14 14 0 0 1 20 4z" fill="#fff"/><circle cx="20" cy="18" r="5" fill="#1f2d4c"/></svg></div>Place the order</div>
  <div class="step" style="left:523px"><div class="ring">
    <svg width="48" height="48" viewBox="0 0 48 48"><path d="M8 10h9l3 9-5 3c3 6 7 10 12 12l3-5 9 3v9C22 41 7 26 8 10z" fill="none" stroke="#fff" stroke-width="3"/><path d="M28 6a14 14 0 0 1 14 14M36 4v8h-8" stroke="#fff" stroke-width="3" fill="none"/></svg></div>Get a callback within the hour</div>
  <div class="step" style="left:751px"><div class="ring">
    <svg width="46" height="46" viewBox="0 0 46 46"><rect x="4" y="8" width="38" height="34" rx="3" fill="#fff"/><rect x="4" y="8" width="38" height="8" fill="#fff"/><g fill="#1f2d4c"><rect x="10" y="20" width="6" height="5"/><rect x="20" y="20" width="6" height="5"/><rect x="30" y="20" width="6" height="5"/><rect x="10" y="30" width="6" height="5"/><rect x="20" y="30" width="6" height="5"/><rect x="30" y="30" width="6" height="5"/></g><rect x="12" y="3" width="4" height="9" fill="#fff"/><rect x="30" y="3" width="4" height="9" fill="#fff"/></svg></div>Set date and location</div>
  <div class="step" style="left:932px"><div class="ring">
    <svg width="52" height="40" viewBox="0 0 52 40"><path d="M2 10l10-4 8 4 8-4 10 2 12 2v14l-8 4-10 8-6-2-6-4-8-6-10-2z" fill="#fff"/><path d="M18 16l8 6M22 24l6 4" stroke="#1f2d4c" stroke-width="2"/></svg></div>We will come to you</div>
</section>

<div class="abs cats-title"><h2 class="section-title">Categories</h2><div class="rule"></div></div>

<div class="card active" style="left:90px;top:1440px">
  <div class="icon"><svg width="22" height="22"><circle cx="11" cy="11" r="10" fill="#fff"/></svg></div>
  <div class="body"><h5>Orchard Phone</h5><p>Lorem ipsum dolor sit amet,<br>tur adipisicing elit. Earum sunt ut<br>dolorem laboriosam culpa</p></div>
</div>
<div class="card" style="left:437px;top:1440px">
  <div class="icon"><svg width="22" height="22"><circle cx="11" cy="11" r="10" fill="#fff"/></svg></div>
  <div class="body"><h5>Droidline Phone</h5><p>Lorem ipsum dolor sit amet,<br>tur adipisicing elit. Earum sunt ut<br>dolorem laboriosam culpa</p></div>
</div>
<div class="card" style="left:784px;top:1440px">
  <div class="icon"><svg width="22" height="22"><rect x="1" y="1" width="20" height="20" fill="#fff"/></svg></div>
  <div class="body"><h5>Panes Phone</h5><p>Lorem ipsum dolor sit amet,<br>tur adipisicing elit. Earum sunt ut<br>dolorem laboriosam culpa</p></div>
</div>
<div class="card" style="left:90px;top:1598px">
  <div class="icon"><svg width="16" height="26" viewBox="0 0 16 26"><rect x="1" y="1" width="14" height="24" rx="2" fill="none" stroke="#fff" stroke-width="2"/><rect x="4" y="5" width="8" height="12" fill="#fff"/><circle cx="8" cy="21" r="1.5" fill="#fff"/></svg></div>
  <div class="body"><h5>Berrytone Phone</h5><p>Lorem ipsum dolor sit amet,<br>tur adipisicing elit. Earum sunt ut<br>dolorem laboriosam culpa</p></div>
</div>
<div class="card" style="left:437px;top:1598px">
  <div class="icon"><svg width="26" height="28" viewBox="0 0 26 28" fill="none" stroke="#fff" stroke-width="2.5"><rect x="3" y="3" width="8" height="10" rx="2"/><rect x="15" y="15" width="8" height="10" rx="2"/><path d="M7 13v6c0 4 4 4 8 2M19 15V9c0-4-4-4-8-2"/></svg></div>
  <div class="body"><h5>Phone Accessory</h5><p>Lorem ipsum dolor sit amet,<br>tur adipisicing elit. Earum sunt ut<br>dolorem laboriosam culpa</p></div>
</div>
<div class="card" style="left:784px;top:1598px">
  <div class="icon"><svg width="30" height="26" viewBox="0 0 30 26"><path d="M3 18l12-7 12 7-12 7z" fill="none" stroke="#fff" stroke-width="2"/><path d="M15 2c2 3 3 5 3 6a3 3 0 0 1-6 0c0-1 1-3 3-6z" fill="#fff"/></svg></div>
  <div class="body"><h5 style="text-transform:none">Water Damaged Phone</h5><p>Lorem ipsum dolor sit amet,<br>tur adipisicing elit. Earum sunt ut<br>dolorem laboriosam culpa</p></div>
</div>

<div class="abs quotes-title"><h2 class="section-title">What Clients Say ?</h2><div class="rule"></div></div>

<div class="quote" style="left:90px">
  <p>Lorem ipsum dolor sit ametconsectetur adipisi cing elit. Earum sunt ut dolorem laboriosam culpa excepturi sed distinctio eius!</p>
  <div class="avatar" role="img" aria-label="Portrait photo of the client"></div>
  <div class="who">MARK DELLAWAY<span>Lorem ipsum</span></div>
</div>
<div class="quote" style="left:434px">
  <p>Lorem ipsum dolor sit ametconsectetur adipisi cing elit. Earum sunt ut dolorem laboriosam culpa excepturi sed distinctio eius!</p>
  <div class="avatar" role="img" aria-label="Portrait photo of the client"></div>
  <div class="who">MARK DELLAWAY<span>Lorem ipsum</span></div>
</div>
<div class="quote" style="left:777px">
  <p>Lorem ipsum dolor sit ametconsectetur adipisi cing elit. Earum sunt ut dolorem laboriosam culpa excepturi sed distinctio eius!</p>
  <div class="avatar" role="img" aria-label="Portrait photo of the client"></div>
  <div class="who">MARK DELLAWAY<span>Lorem ipsum</span></div>
</div>

<section class="abs partners" aria-label="Partner brands">
  <div class="partner" style="left:90px;width:195px"></div>
  <div class="partner" style="left:402px;width:150px"></div>
  <div class="partner" style="left:676px;width:150px"></div>
  <div class="partner" style="left:960px;width:140px"></div>
</section>

<footer class="abs footer">
  <h6 style="left:95px">CONTACTS</h6>
  <div class="line" style="left:122px;top:92px"><svg width="10" height="14" viewBox="0 0 10 14"><path d="M5 0a5 5 0 0 1 5 5c0 4-5 9-5 9S0 9 0 5a5 5 0 0 1 5-5z" fill="#fff"/><circle cx="5" cy="5" r="2" fill="#17233f"/></svg>22 Linden Quay, Unit B<br>Westbrook, NV 10482</div>
  <div class="line" style="left:127px;top:158px"><svg width="12" height="12" viewBox="0 0 12 12"><path d="M1 1h3l1 3-2 1c1 2 2 3 4 4l1-2 3 1v3C5 11 1 7 1 1z" fill="#fff"/></svg>1-800-555-0199</div>
  <div class="line" style="left:127px;top:209px"><svg width="12" height="12" viewBox="0 0 12 12"><rect x="1" y="4" width="10" height="6" fill="#fff"/><rect x="3" y="1" width="6" height="4" fill="#fff"/></svg>1-800-555-0123</div>

  <h6 style="left:393px">QUICK LINKS</h6>
  <ul class="links"><li>Home</li><li>About</li><li>Services</li><li>Experts</li><li>Pricing</li><li>Contact us</li></ul>

  <h6 style="left:617px">NEWSLETTER</h6>
  <div class="news"><p>Enter your e-mail and subscribe to our newsletter</p></div>
  <div class="email">E - mail</div>
  <div class="subscribe">SUBSCRIBE</div>

  <h6 style="left:926px">FOLLOW US</h6>
  <div class="follow"><span>Linkr</span><span>Chirpa</span><span>Pixo</span><span>Pinlo</span><span>Vidz</span><span>Plusr</span></div>
</footer>
<div class="abs bottom">Copyright © . All Rights Reserved</div>

</body>
</html>
```